Corporate Web Redesign Project - coded

We would like redesign/refresh of our current site that would allow us to increase the depth of content and create a high quality impression for visitors.

Current site - http://corvanisystems.example/

A previous web redesign project has improved our site but it has not really reached the level we require.

Our customers are global, blue chip, organisations and a professional, corporate style of site is required.

Please note we would prefer a coded website to a just a design. We are happy to provide a zip of our current site if required.
Updates

                                   

Target Market(s)

Global oil and gas producers, KT, Pardo, Valmira etc.

Industry/Entity Type

It Professional

Requirements
Must have
• Design should support the level of content we currently have in the existing sitemap - although it should be expandable a site design for a large / complex site would not be appropriate

All current content / pages to be reflected in design

Must be visually appealing

Intuitive and clear navigation that is expandable

Display a high level of professionalism

Use a consistent palette of colours that complements our logo

Clean and organized layout

A way to capture visitor’s information or Call to action (i.e. contact link or form) on every page

Prominent Contact Information
Should not have
• Flash

```html
<!DOCTYPE html>
<html lang="en">
<head>
<meta charset="utf-8">
<title>Corvani Systems</title>
<link href="https://fonts.googleapis.com/css2?family=Open+Sans:wght@400;600&family=Hind:wght@400;500&display=swap" rel="stylesheet">
<style>
:root{
  --olive:#7a8c45;
  --teal:#5a8fa0;
  --heading:#2f5060;
  --green-heading:#4e6b33;
  --text:#5a5a5a;
  --dark:#222;
  --footer:#262626;
  --rule:#e2e2e2;
  --link:#3f6b2a;
}
*{box-sizing:border-box;margin:0;padding:0}
html,body{width:1200px;height:1129px;overflow:hidden;background:#fff}
body{font-family:"Hind",Arial,sans-serif;color:var(--text);position:relative}
.hero{position:absolute;left:0;top:0;width:1200px;height:512px;
  background:linear-gradient(180deg,#c9c1b2 0%,#e8cdb1 35%,#f1d2b4 62%,#a59c96 80%,#6d7079 100%)}
.hero-rig{position:absolute;left:560px;top:90px;width:520px;height:422px;
  background:linear-gradient(180deg,rgba(120,100,90,.25),rgba(70,60,55,.55));border-radius:8px 8px 0 0}
.header{position:absolute;left:100px;top:19px;width:1000px;height:82px;background:#fff;border-bottom:1px solid #bbb;display:flex;align-items:center}
.brand{margin-left:12px;display:flex;align-items:center;gap:8px;font-family:"Open Sans",sans-serif;font-weight:600;font-size:20px;color:var(--heading)}
.brand-mark{width:16px;height:16px;border-radius:50%;background:var(--teal)}
.nav{position:absolute;right:0;top:0;height:82px;display:flex;font-size:15px;color:#333}
.nav a{display:flex;align-items:center;padding:0 20px;text-decoration:none;color:inherit}
.nav a.active{background:var(--olive);color:#fff;padding:0 10px;margin-right:8px}
.hero-copy{position:absolute;left:114px;top:236px;width:300px}
.hero-copy h1{font-family:"Open Sans",sans-serif;font-weight:600;font-size:21px;color:var(--heading)}
.hero-copy p{font-size:13px;line-height:18px;margin-top:6px;color:#6a6055}
.btn-contact{position:absolute;left:114px;top:336px;width:114px;height:37px;background:linear-gradient(#333,#000);color:#fff;border-radius:3px;font-family:"Open Sans",sans-serif;font-weight:600;font-size:18px;display:flex;align-items:center;justify-content:center;border:1px solid #111}
.band{position:absolute;left:0;top:512px;width:1200px;height:7px;background:#b9b9b9}
.services{position:absolute;left:100px;top:512px;width:1000px;height:146px;display:flex}
.service{width:250px;border-top:7px solid var(--teal);border-right:1px solid var(--rule);padding:20px 13px 0;position:relative}
.service:first-child{border-left:1px solid var(--rule)}
.service.alt{border-top-color:#86a040}
.service h2{font-family:"Open Sans",sans-serif;font-weight:400;font-size:19px;color:var(--heading)}
.service.alt h2{color:var(--green-heading)}
.service p{font-size:12.5px;line-height:16px;margin-top:6px}
.service a{position:absolute;left:13px;top:110px;font-size:12px;color:var(--link);text-decoration:none}
.about{position:absolute;left:101px;top:682px;width:725px}
.about h2,.news h2{font-weight:400;font-size:20px;color:#222}
.about p{font-size:13px;line-height:20px;margin-top:10px}
.btn-more{position:absolute;left:100px;top:884px;width:79px;height:29px;background:linear-gradient(#6c97a6,#3d6878);color:#fff;border-radius:3px;font-family:"Open Sans",sans-serif;font-weight:600;font-size:12px;display:flex;align-items:center;justify-content:center}
.news{position:absolute;left:850px;top:682px;width:250px}
.news-item{margin-top:10px;font-size:13px;line-height:20px;overflow:hidden}
.news-item+.news-item{margin-top:22px}
.thumb{float:left;width:56px;height:56px;margin:0 9px 0 0}
.news-item h3{font-weight:500;font-size:14.5px;color:#222;line-height:16px;margin-bottom:4px}
.partners-title{position:absolute;left:100px;top:936px;width:1000px;display:flex;align-items:center;gap:16px;font-size:19px;color:#333}
.partners-title::after{content:"";flex:1;height:1px;background:var(--rule)}
.partners{position:absolute;left:100px;top:980px;width:1000px;height:56px;display:flex;justify-content:space-between;align-items:center;font-family:"Open Sans",sans-serif;font-weight:600;font-size:15px}
.partners span{width:100px;text-align:center}
.footer{position:absolute;left:0;top:1074px;width:1200px;height:55px;background:var(--footer);color:#eee;font-size:12.5px}
.footer .copy{position:absolute;left:116px;top:19px}
.social{position:absolute;right:100px;top:17px;display:flex;align-items:center;gap:8px}
.social i{display:block;width:21px;height:21px;background:#5a8fb8;border-radius:2px}
</style>
</head>
<body>
<div class="hero" role="img" aria-label="Offshore drilling platform at sea under a warm sky"><div class="hero-rig"></div></div>

<header class="header">
  <div class="brand"><span class="brand-mark"></span>Corvani Systems</div>
  <nav class="nav">
    <a class="active" href="#">Home</a><a href="#">News</a><a href="#">About Us</a><a href="#">Solutions</a><a href="#">Technologies</a>
  </nav>
</header>

<div class="hero-copy">
  <h1>The Business Of Drilling Wells</h1>
  <p>Sed ut perspiciatis unde omnis iste natus error sit voluptatem accusantium doloremque laudantium, totam rem aperiam...</p>
</div>
<div class="btn-contact">Contact Us</div>

<div class="band"></div>
<section class="services">
  <div class="service"><h2>Time &amp; Cost Estimation</h2><p>PTX delivers a standardized systematic approach to understanding project risk....</p><a href="#">Read more »</a></div>
  <div class="service alt"><h2>Material &amp; Cost Control</h2><p>MTX has been helping companies optimize materials and cost tracking process since 1992....</p><a href="#">Read more »</a></div>
  <div class="service"><h2>Lesson Learned</h2><p>LRX is an advanced lesson learned &amp; knowledge system for use in the energy industry....</p><a href="#">Read more »</a></div>
  <div class="service alt"><h2>Services &amp; Consulting</h2><p>Sucessful software implementations rely on people and processes to deliver results....</p><a href="#">Read more »</a></div>
</section>

<section class="about">
  <h2>About Us</h2>
  <p>From early phase evaluation through planning, execution and post analysis of wells, we deliver the tools, processes and people required to facilitate major performance improvement and cost savings.</p>
  <p style="margin-top:12px">Our solutions are used in more than 30 countries to support operations ranging from a single well to global deployments with Major Operators.<br>Sed ut perspiciatis unde omnis iste natus error sit voluptatem accusantium doloremque laudantium, totam rem aperiam, eaque ipsa quae ab illo inventore veritatis et quasi architecto beatae vitae dicta sunt explicabo. Nemo enim ipsam voluptatem quia voluptas sit aspernatur aut odit aut fugit,...</p>
</section>
<div class="btn-more">Read More</div>

<aside class="news">
  <h2>Latest News</h2>
  <div class="news-item"><div class="thumb" role="img" aria-label="Office building exterior" style="background:linear-gradient(#9fb0bf,#7b7a70)"></div><h3>PTX Selected by Harlow</h3>Harlow Energy Ltd has selected PTX as the solution to provide probabilistic time and cost estimates for its drilling operations....</div>
  <div class="news-item"><div class="thumb" role="img" aria-label="Portrait of a company representative" style="background:linear-gradient(#8a8270,#4a4540)"></div><h3>MTX Implementation</h3>Northmere selects MTX to support its materials, logistics &amp; cost management processes....</div>
</aside>

<div class="partners-title">Our Partner</div>
<div class="partners">
  <span style="color:#1d5fa8">Valmira</span>
  <span style="color:#a0521c">Ostrel</span>
  <span style="color:#c9a31a">Dunmore</span>
  <span style="color:#777">Harlow</span>
  <span style="color:#5aa51e">KT</span>
  <span style="color:#1e3f7a">Northmere</span>
  <span style="color:#1f6b3a">Brannock</span>
  <span style="color:#1d5fa8">Valmira</span>
</div>

<footer class="footer">
  <div class="copy">Copyright © 2013 Corvani Systems Ltd.All Rights Reserved</div>
  <div class="social">Stay Connected:&nbsp;<i></i><i></i><i></i></div>
</footer>
</body>
</html>
```